Gourmet cookie company needs a label designed

We need a label designed for a new cookie company. We make mini cookies. The labels will be placed on either white tins or clear containers. We would like some bright and eye catching label although not child like. Our target customer is adults not kids.
Any color/colors acceptable. The initial label will be a square 4" label but the design should also be able to be formatted to fit on a round label as well in the future.

Text on label: Henrietta's Little Oven Company; Chocolate Chip; All Natural; New Wt. 8.0oz

```html
<!DOCTYPE html>
<html lang="en">
<head>
<meta charset="utf-8">
<title>Henrietta's Little Oven Company – Chocolate Chip Label</title>
<link rel="stylesheet" href="https://fonts.googleapis.com/css2?family=Grand+Hotel&family=Montserrat:wght@400;500&display=swap">
<style>
  :root {
    --backdrop-light: #ffffff;
    --backdrop-dark: #d4d4d4;
    --label-red: #d81200;
    --label-white: #ffffff;
    --ribbon-coral: #ff8469;
    --ribbon-fold: #a80e00;
  }
  html, body {
    margin: 0;
    padding: 0;
    width: 1200px;
    height: 900px;
    overflow: hidden;
  }
  body {
    background: radial-gradient(ellipse at center, var(--backdrop-light) 35%, var(--backdrop-dark) 100%);
  }
  .label {
    position: absolute;
    left: 0;
    top: 0;
    width: 1200px;
    height: 900px;
  }
  .label-face { fill: var(--label-red); }
  .outer-ring { fill: none; stroke: var(--label-white); stroke-width: 1.2; }
  .inner-disc { fill: var(--label-white); }
  .ribbon-band, .ribbon-tail { fill: var(--ribbon-coral); }
  .ribbon-fold { fill: var(--ribbon-fold); }
  .brand-name {
    font-family: "Grand Hotel", cursive;
    font-size: 84px;
    fill: var(--label-red);
  }
  .brand-tagline {
    font-family: "Montserrat", sans-serif;
    font-weight: 400;
    font-size: 9.5px;
    letter-spacing: 3.2px;
    fill: var(--label-red);
  }
  .flavour {
    font-family: "Montserrat", sans-serif;
    font-weight: 400;
    font-size: 17px;
    letter-spacing: 4.2px;
    fill: var(--label-white);
  }
  .claim {
    font-family: "Montserrat", sans-serif;
    font-weight: 500;
    font-size: 11px;
    letter-spacing: 2.4px;
    fill: var(--label-red);
  }
  .net-weight {
    font-family: "Montserrat", sans-serif;
    font-weight: 500;
    font-size: 8.5px;
    letter-spacing: 1.6px;
    fill: var(--label-red);
  }
</style>
</head>
<body>
<svg class="label" viewBox="0 0 1200 900" xmlns="http://www.w3.org/2000/svg">
  <rect class="label-face" x="332" y="182" width="535" height="535"/>
  <circle class="outer-ring" cx="600" cy="449" r="201"/>
  <circle class="inner-disc" cx="600" cy="450" r="182"/>

  <g class="ribbon">
    <polygon class="ribbon-tail" points="362,508 407,508 407,563 362,563 381,535.5"/>
    <polygon class="ribbon-fold" points="388,545 407,545 407,561"/>
    <polygon class="ribbon-tail" points="838,508 793,508 793,563 838,563 819,535.5"/>
    <polygon class="ribbon-fold" points="812,545 793,545 793,561"/>
    <rect class="ribbon-band" x="388" y="490" width="424" height="55"/>
  </g>

  <text class="brand-name" x="600" y="438" text-anchor="middle">Henrietta's</text>
  <text class="brand-tagline" x="742" y="465" text-anchor="end">LITTLE OVEN COMPANY</text>

  <text class="flavour" x="600" y="523" text-anchor="middle">CHOCOLATE CHIP</text>

  <text class="claim" x="600" y="577" text-anchor="middle">ALL NATURAL</text>
  <text class="net-weight" x="600" y="595" text-anchor="middle">NET WT 8oz</text>
</svg>
</body>
</html>
```